Business Card Design

We need a design that will also transfer to car decals
We need a design that will speak to the average person needing home and office remodeling
The design should be fresh, exciting, easy to read in a glance and unique
We would like a die-cut tool belt
Bright colors and evenly spaced information

Target Market(s)

Home and business owners
Middle and Upper Income property owners
Families and people with fixer upper homes

Industry/Entity Type

Business

Contact Information for Business Card

Looking for the best Bay Area Handyman? Here I am!
RKW Handyman Services does it all at prices regular people can afford.
Electrical, Plumbing, Carpentry, Remodeling, Fencing, Picture and window placement, Hauling ... and anything else you can imagine!
510-473-2918
Serving the Entire Bay Area
Free Estimates! Call us Today to turn your dreams into reality!

Font styles to use
Serif

Requirements
Must have
• Speaks to the average person
stands out among similar industry cards
Nice to have
• fun, comical, you want to hold on to this card
Should not have
• bland colors
look too crowded

```html
<!DOCTYPE html>
<html lang="en">
<head>
<meta charset="utf-8">
<title>RKW Handyman Services – Business Card</title>
<link rel="stylesheet" href="https://fonts.googleapis.com/css2?family=Cinzel:wght@400;700&display=swap">
<style>
  :root {
    --page-bg: #d9d9d9;
    --card-bg: #141414;
    --card-bg-light: #262626;
    --accent: #e8481c;
    --text-light: #ffffff;
    --belt-dark: #3a3532;
    --belt-orange: #e8571f;
    --tool-grey: #b9c3cc;
  }
  * { box-sizing: border-box; margin: 0; padding: 0; }
  html, body {
    width: 1200px;
    height: 900px;
    overflow: hidden;
    background: var(--page-bg);
    font-family: "Cinzel", serif;
  }
  .sheet {
    width: 1200px;
    height: 900px;
    display: flex;
    flex-direction: column;
    align-items: center;
    justify-content: center;
    gap: 28px;
  }
  .card {
    width: 700px;
    height: 400px;
    border-radius: 14px;
    background: radial-gradient(ellipse at 50% 40%, var(--card-bg-light), var(--card-bg) 75%);
    color: var(--text-light);
    text-align: center;
    display: flex;
    flex-direction: column;
    align-items: center;
    box-shadow: 0 6px 18px rgba(0,0,0,0.35);
  }

  /* Services side */
  .card-services { justify-content: center; padding: 0 40px; }
  .brand-name {
    color: var(--accent);
    font-weight: 700;
    font-size: 30px;
    margin-bottom: 14px;
  }
  .service-list {
    font-weight: 700;
    font-size: 17px;
    line-height: 1.35;
    margin-bottom: 28px;
  }
  .call-to-action {
    color: var(--accent);
    font-weight: 700;
    font-size: 20px;
    margin-bottom: 6px;
  }
  .phone {
    font-weight: 700;
    font-size: 42px;
    margin-bottom: 18px;
  }
  .coverage {
    font-weight: 700;
    font-size: 21px;
  }

  /* Front side */
  .card-front { justify-content: space-between; padding: 34px 30px 30px; }
  .headline {
    font-weight: 700;
    font-size: 20px;
  }
  .tool-belt {
    width: 560px;
    height: 190px;
  }
  .slogan-main {
    color: var(--accent);
    font-weight: 700;
    font-size: 28px;
    line-height: 1.1;
  }
  .slogan-main .intro { text-transform: lowercase; font-size: 24px; }
  .slogan-sub {
    font-weight: 700;
    font-size: 17px;
    text-transform: lowercase;
    margin-top: 4px;
  }
</style>
</head>
<body>
<main class="sheet">
  <section class="card card-services">
    <h1 class="brand-name">RKW Handyman Services</h1>
    <p class="service-list">Electrical, Plumbing, Carpentry, Remodeling,<br>Fencing, Picture and Window Placement, Hauling<br>and Anything Else You Can Imagine!</p>
    <p class="call-to-action">Call us Today to turn your Dreams into Reality!</p>
    <p class="phone">510-473-2918</p>
    <p class="coverage">Serving The Entire Bay Area Free Estimates!</p>
  </section>

  <section class="card card-front">
    <p class="headline">Looking for the Best Bay Area Handyman?</p>
    <svg class="tool-belt" viewBox="0 0 560 190" role="img" aria-label="Illustration of a tool belt holding a screwdriver, pliers, saw, wrench, tape measure and hammer">
      <defs>
        <linearGradient id="belt-tone" x1="0" y1="0" x2="1" y2="1">
          <stop offset="0" stop-color="var(--belt-orange)"/>
          <stop offset="0.5" stop-color="var(--belt-dark)"/>
          <stop offset="1" stop-color="var(--tool-grey)"/>
        </linearGradient>
      </defs>
      <rect x="0" y="0" width="560" height="190" rx="20" fill="url(#belt-tone)" opacity="0.85"/>
    </svg>
    <div>
      <p class="slogan-main"><span class="intro">Here I am!</span> RKW Handyman Services</p>
      <p class="slogan-sub">Does it all at prices regular people can afford.</p>
    </div>
  </section>
</main>
</body>
</html>
```